Hi Designers,

I will need 4 web pages designed. The web page looks like an App (if you click on the logo, or the icon on an iPad, it will take you to the website), but it is still a webpage.

Please check the attachment on this brief to understand what specific pages I need to be designed.

A .PSD (straight-up PhotoShop image) as final deliverable is fine, as long as you give us the exact “web color numbers”.

The design is for desktop and iPad but in a single unified web application, NOT separate web app and (native) iPad app.

Details:

Brightwell Ledger Advisory Group is developing a browser-based application for use on any mobile device or desktop. The app will be used by corporations to communicate with their employees regarding legal, regulatory and company requirements for conducting business. The app is known as “Harbor Rulebook Hub.” When the user clicks on the icon for Harbor Rulebook Hub, they will enter a site full of information that a company deems necessary for the employee to do his/her job. There are several content sections within the site, including a login page, training, policies, forms, news feeds and blogs.

The application has been built using Microsoft .NET, and fully supports CSS-type skinning; it uses traditional page layouts. We are seeking a product logo concept (image), a master application/desktop icon (image), as well as a full color scheme/theme/skin design for all areas of the application (header area, body text, menu bar, etc.) in the form of a CSS. The look should be clean, crisp and professional; nothing cartoony or whimsical. It should be easy to read and “airy”.

We have sketched prototypes for the basic application page layout that we can send as a next step of the process.
Updates

Screen shots have been uploaded to this project.  Please use them to guide your design.

Dear designers,

I apologize for the delay in providing feedback. My partners and I will provide feedback in a few days. Thank you for your patience.

Industry/Entity Type

Business

Font styles to use
Other font styles liked:
• see font on screen shots when uploaded

```html
<!DOCTYPE html>
<html lang="en">
<head>
<meta charset="utf-8">
<title>Corvane Labs – Sign In</title>
<link href="https://fonts.googleapis.com/css2?family=Roboto+Condensed:wght@400;700&display=swap" rel="stylesheet">
<style>
  :root {
    --header-navy: #0b2a4f;
    --header-rule: #3f6f9c;
    --body-blue: #1d4f7f;
    --body-glow: #5f8fb8;
    --panel-frame: #0e3252;
    --label-ink: #0c2b4a;
    --field-top: #ffffff;
    --field-bottom: #e2e4e6;
    --field-edge: #0f3a5e;
    --link-cream: #f3e7a6;
    --button-top: #7fb1e3;
    --button-bottom: #3d78b8;
    --button-ink: #000000;
    --title-grey: #dcdcdc;
    --hub-blue: #6fc2f6;
  }
  * { box-sizing: border-box; margin: 0; padding: 0; }
  html, body { width: 1200px; height: 800px; overflow: hidden; }
  body {
    font-family: "Roboto Condensed", "Arial Narrow", sans-serif;
    background: radial-gradient(ellipse 520px 340px at 600px 480px, var(--body-glow), var(--body-blue) 75%, #1a4975);
    position: relative;
  }
  .site-header {
    position: absolute; left: 0; top: 0; width: 1200px; height: 178px;
    background: var(--header-navy);
    border-bottom: 1px solid var(--header-rule);
    text-align: center;
  }
  .brand-dot {
    position: absolute; left: 575px; top: 22px; width: 50px; height: 50px;
    border-radius: 50%; background: #3a9ad9;
  }
  .brand-name {
    position: absolute; left: 0; width: 100%; top: 80px;
    font-size: 66px; font-weight: 700; color: var(--title-grey); line-height: 1;
  }
  .login-panel {
    position: absolute; left: 235px; top: 206px; width: 766px; height: 414px;
    border: 8px solid var(--panel-frame); border-radius: 14px;
  }
  .field-label {
    position: absolute; left: 101px; font-size: 28px; color: var(--label-ink);
  }
  .field-input {
    position: absolute; left: 101px; width: 513px; height: 53px;
    border: 2px solid var(--field-edge); border-radius: 6px;
    background: linear-gradient(var(--field-top), var(--field-bottom));
  }
  .remember-box {
    position: absolute; left: 101px; top: 239px; width: 36px; height: 35px;
    border: 2px solid var(--field-edge); border-radius: 6px;
    background: linear-gradient(var(--field-top), var(--field-bottom));
  }
  .remember-text {
    position: absolute; left: 148px; top: 242px; font-size: 23px; color: var(--link-cream);
  }
  .sign-in-button {
    position: absolute; left: 266px; top: 320px; width: 182px; height: 58px;
    border: 2px solid #2a5f95; border-radius: 8px;
    background: linear-gradient(var(--button-top), var(--button-bottom));
    font-family: inherit; font-size: 38px; color: var(--button-ink);
  }
  .hub-rule {
    position: absolute; top: 703px; height: 1px; background: #4f8fc8;
  }
  .hub-mark {
    position: absolute; left: 508px; top: 660px; width: 80px; height: 80px;
    border-radius: 50%; background: var(--hub-blue);
  }
  .hub-name {
    position: absolute; left: 622px; top: 644px;
    font-size: 31px; font-weight: 700; line-height: 40px; color: var(--hub-blue);
  }
</style>
</head>
<body>
  <header class="site-header">
    <div class="brand-dot"></div>
    <h1 class="brand-name">Corvane Labs</h1>
  </header>

  <form class="login-panel">
    <label class="field-label" style="top:26px">Username</label>
    <div class="field-input" style="top:58px"></div>
    <label class="field-label" style="top:136px">Password</label>
    <div class="field-input" style="top:168px"></div>
    <div class="remember-box"></div>
    <span class="remember-text">Keep me signed in | Forgot Password?</span>
    <button class="sign-in-button" type="button">Sign In</button>
  </form>

  <div class="hub-rule" style="left:234px;width:246px"></div>
  <div class="hub-rule" style="left:800px;width:198px"></div>
  <div class="hub-mark"></div>
  <div class="hub-name">Harbor<br>Rulebook<br>Hub</div>
</body>
</html>
```